Marbella Specialty Coffee needs a Packaging design

We need packaging design for coffee that suits our brand identity, that is the best quality in Mexico.
We only sell mexican coffee with Q scores above 80
We are evaluating 3 types of packaging: Bag, Box and Cillinder can
The specific package format will be decided based on the designs that we get.

Target Market(s)

Coffee experts and enthusiast.
People that relate the Coffee consumption and experience with wine tasting and Bon Vivant way

Requirements
Should not have
• Photos any mexican cliché

```html
<!DOCTYPE html>
<html lang="en">
<head>
<meta charset="utf-8">
<title>Marbella Specialty Coffee – Packaging Range</title>
<link rel="stylesheet" href="https://fonts.googleapis.com/css2?family=Sorts+Mill+Goudy&family=Oswald:wght@500&family=Inter:wght@600&display=swap">
<style>
  :root {
    --page-bg: #ffffff;
    --bag-black: #1b1b1b;
    --bag-sheen: #2a2a2a;
    --zip-line: #0d0d0d;
    --ink-white: #ffffff;
    --label-black: #000000;
    --single-origin: #e0262a;
    --season-blend: #a3a9ac;
    --mocha-blend: #a2bd8e;
  }
  * { margin: 0; padding: 0; box-sizing: border-box; }
  html, body {
    width: 1200px; height: 1000px; overflow: hidden;
    background: var(--page-bg);
  }
  .range {
    position: relative; width: 1200px; height: 1000px;
  }
  .bag {
    position: absolute; top: 212px;
    width: 337px; height: 535px;
    background: linear-gradient(160deg, var(--bag-sheen) 0%, var(--bag-black) 45%, var(--bag-black) 100%);
    border-radius: 3px;
  }
  .bag--single { left: 78px; }
  .bag--season { left: 432px; }
  .bag--mocha  { left: 788px; }
  .bag__zip {
    position: absolute; left: 0; right: 0; top: 33px;
    height: 2px; background: var(--zip-line);
  }
  .bag__valve {
    position: absolute; left: 154px; top: 82px;
    width: 26px; height: 26px; border-radius: 50%;
    border: 2px solid var(--zip-line);
  }
  .brand {
    position: absolute; left: 58px; top: 160px;
    color: var(--ink-white);
    font-family: "Sorts Mill Goudy", Georgia, serif;
  }
  .brand__name {
    font-size: 66px; line-height: 1; letter-spacing: 1px;
  }
  .brand__tagline {
    position: absolute; left: 172px; top: 76px;
    font-size: 17px; line-height: 18px; white-space: nowrap;
  }
  .variety {
    position: absolute; left: 125px; top: 328px;
    width: 86px; height: 132px;
    color: var(--ink-white);
    text-align: center;
  }
  .variety--single { background: var(--single-origin); }
  .variety--season { background: var(--season-blend); }
  .variety--mocha  { background: var(--mocha-blend); }
  .variety__tab {
    position: absolute; left: 27px; top: 0;
    width: 32px; height: 42px; background: var(--label-black);
  }
  .variety__name {
    position: absolute; left: 0; right: 0; top: 52px;
    font-family: "Oswald", "Arial Narrow", sans-serif;
    font-weight: 500; font-size: 20px; line-height: 21px;
    text-transform: uppercase;
  }
  .variety__cup {
    position: absolute; left: 30px; top: 99px;
    width: 26px; height: 22px;
  }
  .weight {
    position: absolute; left: 95px; top: 470px; width: 146px;
    text-align: center; color: var(--ink-white);
    font-family: "Inter", Arial, sans-serif;
    font-weight: 600; font-size: 11px;
  }
</style>
</head>
<body>
<main class="range">

  <section class="bag bag--single">
    <div class="bag__zip"></div>
    <div class="bag__valve"></div>
    <div class="brand">
      <div class="brand__name">Marbella</div>
      <div class="brand__tagline">Specialty<br>Coffee</div>
    </div>
    <div class="variety variety--single">
      <div class="variety__tab"></div>
      <div class="variety__name">Single<br>Origin</div>
      <svg class="variety__cup" viewBox="0 0 26 22" fill="none" stroke="#fff" stroke-width="1.4">
        <path d="M10 1c-2 2 2 3 0 5M14 1c-2 2 2 3 0 5"/>
        <path d="M5 8h14v4a7 7 0 0 1-14 0z"/>
        <path d="M19 10h2a2 2 0 0 1 0 4h-2.5"/>
        <path d="M2 20h22"/>
      </svg>
    </div>
    <div class="weight">500 g &nbsp;|&nbsp; 1.1 lbs</div>
  </section>

  <section class="bag bag--season">
    <div class="bag__zip"></div>
    <div class="bag__valve"></div>
    <div class="brand">
      <div class="brand__name">Marbella</div>
      <div class="brand__tagline">Specialty<br>Coffee</div>
    </div>
    <div class="variety variety--season">
      <div class="variety__tab"></div>
      <div class="variety__name">Season<br>Blend</div>
      <svg class="variety__cup" viewBox="0 0 26 22" fill="none" stroke="#fff" stroke-width="1.4">
        <path d="M10 1c-2 2 2 3 0 5M14 1c-2 2 2 3 0 5"/>
        <path d="M5 8h14v4a7 7 0 0 1-14 0z"/>
        <path d="M19 10h2a2 2 0 0 1 0 4h-2.5"/>
        <path d="M2 20h22"/>
      </svg>
    </div>
    <div class="weight">500 g &nbsp;|&nbsp; 1.1 lbs</div>
  </section>

  <section class="bag bag--mocha">
    <div class="bag__zip"></div>
    <div class="bag__valve"></div>
    <div class="brand">
      <div class="brand__name">Marbella</div>
      <div class="brand__tagline">Specialty<br>Coffee</div>
    </div>
    <div class="variety variety--mocha">
      <div class="variety__tab"></div>
      <div class="variety__name">Mocha<br>Blend</div>
      <svg class="variety__cup" viewBox="0 0 26 22" fill="none" stroke="#fff" stroke-width="1.4">
        <path d="M10 1c-2 2 2 3 0 5M14 1c-2 2 2 3 0 5"/>
        <path d="M5 8h14v4a7 7 0 0 1-14 0z"/>
        <path d="M19 10h2a2 2 0 0 1 0 4h-2.5"/>
        <path d="M2 20h22"/>
      </svg>
    </div>
    <div class="weight">500 g &nbsp;|&nbsp; 1.1 lbs</div>
  </section>

</main>
</body>
</html>
```